HVAC company business card design

We need a business card design for a HVAC company. The design must look professional. Both sides will be used. The total data to be on the business card is
Name
Position
Email
Direct Phone/Moile Phone
Company Contacts /Address, Phone, Fax, web)
All data will be submit once the design is confirmed. For generic purposes use;
Emre Toksoy
Managing Director
+902324815263 (Mobile)
4712 Sokak No: 9 KBSE Yenikent IZMIR TURKEY
Tel: +902324815263 Fax : +902324815269
www.luvon.com.tr

Target Market(s)

HVAC

Industry/Entity Type

Business

Contact Information for Business Card

The total data to be on the business card is
Name
Position
Email
Direct Phone/Moile Phone
Emre Toksoy
Managing Director
+902324815263 (Mobile)
www.luvon.com.tr
The BC will use both sides of the card. The front will include the full logo and the details for the business card holder. The business card can be divided into vertical/horizontal or to a special shape. The common data like the company address/phone/fax should be indicated elsewehere. The back can contain some part or the whole logo and must contain the web address.

Font styles to use
Serif
Sans Serif

Colors
0355a3
cfdfed

Requirements
Should not have
• Please be careful with the fonts, it shouldnt be too small or too big and must not interfere with the logo fonts. If you need to use a curvy shape please do not use as the logo is already curvy or use the curves from the logo (if it looks good, otherwise forget it)
• We are not in favor of pictograms, only if they are perfect use them.

```html
<!DOCTYPE html>
<html lang="en">
<head>
<meta charset="utf-8">
<title>Luvon Business Card</title>
<link rel="stylesheet" href="https://fonts.googleapis.com/css2?family=Michroma&display=swap">
<style>
  :root {
    --brand-blue: #0355a3;
    --brand-ice: #cfdfed;
    --gradient-deep: #3a76b8;
    --gradient-light: #c4d8ea;
    --ink: #3d4559;
    --logo-ink: #3f4a63;
    --mark-blue: #1f6fc2;
    --paper: #ffffff;
    --edge: #8a1f2b;
  }
  * { margin: 0; padding: 0; box-sizing: border-box; }
  html, body {
    width: 1200px;
    height: 652px;
    overflow: hidden;
    background: var(--paper);
  }
  .card {
    position: relative;
    width: 1200px;
    height: 652px;
    background: var(--paper);
    border: 2px solid var(--edge);
    overflow: hidden;
    font-family: "Michroma", sans-serif;
    color: var(--ink);
  }
  .card-shapes {
    position: absolute;
    inset: 0;
    width: 100%;
    height: 100%;
  }
  .brand {
    position: absolute;
    left: 80px;
    top: 66px;
    display: flex;
    align-items: center;
    gap: 26px;
  }
  .brand-dot {
    width: 96px;
    height: 96px;
    border-radius: 50%;
    background: var(--mark-blue);
  }
  .brand-name {
    font-size: 66px;
    line-height: 1;
    color: var(--logo-ink);
    letter-spacing: 2px;
  }
  .holder {
    position: absolute;
    right: 56px;
    top: 183px;
    text-align: right;
    color: var(--paper);
    text-transform: uppercase;
  }
  .holder-name {
    font-size: 44px;
    line-height: 1;
    letter-spacing: 1px;
  }
  .holder-role {
    margin-top: 22px;
    font-size: 23px;
    line-height: 1;
    letter-spacing: 1px;
  }
  .contact {
    position: absolute;
    left: 736px;
    top: 356px;
    font-size: 20px;
    line-height: 32px;
    text-transform: uppercase;
    letter-spacing: 1px;
    white-space: nowrap;
  }
  .contact-line.indent { padding-left: 44px; }
  .contact-label { display: inline-block; width: 96px; letter-spacing: 6px; }
  .web {
    position: absolute;
    left: 748px;
    top: 552px;
    font-size: 20px;
    letter-spacing: 1px;
    text-transform: uppercase;
    white-space: nowrap;
  }
</style>
</head>
<body>
<div class="card">
  <svg class="card-shapes" viewBox="0 0 1200 652" preserveAspectRatio="none" aria-hidden="true">
    <defs>
      <linearGradient id="panel-gradient" x1="0" y1="1" x2="1" y2="0">
        <stop offset="0" stop-color="var(--gradient-deep)"/>
        <stop offset="0.55" stop-color="#6d9dcb"/>
        <stop offset="1" stop-color="var(--gradient-light)"/>
      </linearGradient>
      <linearGradient id="band-shadow" x1="0" y1="0" x2="0" y2="1">
        <stop offset="0" stop-color="#1b3552" stop-opacity="0.45"/>
        <stop offset="1" stop-color="#1b3552" stop-opacity="0"/>
      </linearGradient>
    </defs>
    <polygon class="diagonal-panel" points="820,0 1200,0 1200,652 0,652 0,607" fill="url(#panel-gradient)"/>
    <polygon class="name-band-shadow" points="405,304 1200,304 1200,318 420,318" fill="url(#band-shadow)"/>
    <polygon class="name-band" points="405,304 595,153 1200,153 1200,304" fill="var(--brand-blue)"/>
  </svg>

  <div class="brand">
    <span class="brand-dot"></span>
    <span class="brand-name">LUVON</span>
  </div>

  <div class="holder">
    <div class="holder-name">Emre Toksoy</div>
    <div class="holder-role">Managing Director</div>
  </div>

  <div class="contact">
    <div class="contact-line">4712 Sokak No : 9 KBSE</div>
    <div class="contact-line">Yenikent Izmir Turkey</div>
    <div class="contact-line indent"><span class="contact-label">Tel</span>: +90 232 481 52 63</div>
    <div class="contact-line indent"><span class="contact-label">Fax</span>: +90 232 481 52 69</div>
  </div>

  <div class="web">Web: www.luvon.com.tr</div>
</div>
</body>
</html>
```